Business cards Dör Kornhüüs GmbH & Co.KG

We need a uniform business card design template for our employees.
A template should be created to have the same design for all business cards.

Contact Information for Business Card

Firma und Firmierung, Name, Funktion in Unternehmen, Anschrift, Tel. Handynummer, Emailadresse, Internetseite

Colors

Designer to choose colors to be used in the design.

Requirements
Must have
• Our company logo must be on it

```html
<!DOCTYPE html>
<html lang="de">
<head>
<meta charset="utf-8">
<title>Dör Kornhüüs – Visitenkarte</title>
<link rel="stylesheet" href="https://fonts.googleapis.com/css2?family=Open+Sans:wght@400;600&display=swap">
<style>
  :root {
    --page-bg: #e4e5e7;
    --card-bg: #2b2a29;
    --silver: #8d8d8f;
    --lilac: #c593d6;
    --rose: #e0606f;
    --white: #f4f4f4;
  }
  * { box-sizing: border-box; margin: 0; padding: 0; }
  html, body {
    width: 1200px; height: 800px; overflow: hidden;
    background: var(--page-bg);
    font-family: "Open Sans", sans-serif;
  }
  .sheet {
    width: 1200px; height: 800px;
    display: flex; flex-direction: column;
    align-items: center; justify-content: center; gap: 40px;
  }
  .card {
    position: relative;
    width: 560px; height: 320px;
    background: var(--card-bg);
    box-shadow: 0 6px 18px rgba(0,0,0,.25);
  }
  .card-front { display: flex; align-items: center; justify-content: center; }
  .brand-name {
    font-weight: 600; font-size: 40px; letter-spacing: 1px;
    color: var(--silver);
  }
  .card-back .brand-name {
    position: absolute; left: 30px; top: 112px;
    font-size: 30px; color: var(--lilac);
  }
  .divider {
    position: absolute; left: 290px; top: 72px;
    width: 2px; height: 128px; background: var(--lilac);
  }
  .contact {
    position: absolute; left: 318px; top: 80px;
    color: var(--white);
  }
  .person-name { font-weight: 600; font-size: 20px; color: var(--lilac); line-height: 1.1; }
  .person-role { font-size: 15px; margin-bottom: 16px; }
  .contact-line {
    display: flex; align-items: center; gap: 6px;
    font-size: 15px; line-height: 22px;
  }
  .contact-line svg { width: 13px; height: 13px; flex: none; }
  .address {
    position: absolute; left: 0; right: 0; bottom: 48px;
    text-align: center; color: var(--white); font-size: 16px;
  }
</style>
</head>
<body>
<main class="sheet">
  <section class="card card-front">
    <span class="brand-name">Dör Kornhüüs</span>
  </section>

  <section class="card card-back">
    <span class="brand-name">Dör Kornhüüs</span>
    <span class="divider"></span>
    <div class="contact">
      <p class="person-name">Hanna Petersen</p>
      <p class="person-role">Founder</p>
      <p class="contact-line">
        <svg viewBox="0 0 16 16"><path fill="var(--rose)" d="M3.5 1 6 1.5 7 5 5.3 6.4c.9 1.8 2.4 3.3 4.3 4.3L11 9l3.5 1 .5 2.5-2 2C7 14.5 1.5 9 1.5 3z"/></svg>
        +49 4561 20480
      </p>
      <p class="contact-line">
        <svg viewBox="0 0 16 16"><rect x="1" y="3" width="14" height="10" fill="none" stroke="var(--rose)" stroke-width="1.6"/><path d="M1 3l7 6 7-6" fill="none" stroke="var(--rose)" stroke-width="1.6"/></svg>
        hanna@doerkornhuues.de
      </p>
      <p class="contact-line">
        <svg viewBox="0 0 16 16" fill="none" stroke="var(--rose)" stroke-width="1.4"><circle cx="8" cy="8" r="6.5"/><ellipse cx="8" cy="8" rx="2.8" ry="6.5"/><path d="M1.5 8h13"/></svg>
        www.doerkornhuues.de
      </p>
    </div>
    <p class="address">Mühlenstraße 12, 24376 Kappeln an der Schlei</p>
  </section>
</main>
</body>
</html>
```